The Lindenmoor Compass Book

Cover Design for my first book. The book is for elementary school principals who are unhappy and are considering a career change but are afraid to leave. I teach them how to develop emotional fitness and resiliency through thought management so that they can decide whether to stay or leave their position from a place of empowerment. I've attached my podcast artwork for your reference. My publisher suggested not having me on the cover which is fine. I just thought it might be helpful.

Target Market(s)

Elementary School Principals

Industry/Entity Type

Education

Logo Text

The Lindenmoor Compass

Font styles to use
Serif
Sans Serif

Colors
34a6d7
33b8a4
3276b5

Requirements
Must have
• Title, Author name, photo or artwork that captures the essence of the book

```html
<!DOCTYPE html>
<html lang="en">
<head>
<meta charset="utf-8">
<title>The Lindenmoor Compass — Book Cover</title>
<link href="https://fonts.googleapis.com/css2?family=Poppins:wght@300;400;600&display=swap" rel="stylesheet">
<style>
  :root {
    --bg-top: #f2f7fd;
    --bg-bottom: #dce9f8;
    --tile: #c6e0f8;
    --title-blue: #2f86e0;
    --title-deep: #3276b5;
    --line-violet: #8f8ff0;
    --line-cyan: #34c4e8;
    --band: #cfe3f8;
    --author: #3a8fd8;
  }
  * { margin: 0; padding: 0; box-sizing: border-box; }
  html, body { width: 768px; height: 1200px; overflow: hidden; }
  body {
    font-family: "Poppins", sans-serif;
    background: linear-gradient(180deg, var(--bg-top) 0%, var(--bg-bottom) 100%);
  }
  .cover { position: relative; width: 768px; height: 1200px; }
  .flow { position: absolute; inset: 0; }
  .icon-tile {
    position: absolute;
    left: 300px;
    width: 125px;
    height: 125px;
    background: var(--tile);
  }
  .icon-tile--top { top: 156px; }
  .icon-tile--bottom { top: 792px; }
  .title {
    position: absolute;
    top: 425px;
    width: 100%;
    text-align: center;
    color: var(--title-blue);
  }
  .title__small {
    display: block;
    font-weight: 400;
    font-size: 34px;
    letter-spacing: 3px;
    color: var(--title-deep);
    line-height: 1.2;
  }
  .title__main {
    display: block;
    font-weight: 600;
    font-size: 66px;
    letter-spacing: 1px;
    line-height: 1.15;
  }
  .title__sub {
    display: block;
    font-weight: 300;
    font-size: 70px;
    letter-spacing: 2px;
    line-height: 1.1;
  }
  .author-band {
    position: absolute;
    left: 0; bottom: 0;
    width: 100%;
    height: 91px;
    background: var(--band);
    display: flex;
    align-items: center;
    justify-content: center;
  }
  .author {
    font-weight: 400;
    font-size: 27px;
    letter-spacing: 2px;
    color: var(--author);
  }
</style>
</head>
<body>
<main class="cover">
  <svg class="flow" width="768" height="1200" viewBox="0 0 768 1200" aria-hidden="true">
    <line x1="48" y1="245" x2="252" y2="245" stroke="var(--line-violet)" stroke-width="2"/>
    <polyline points="240,237 253,245 240,253" fill="none" stroke="var(--line-violet)" stroke-width="2"/>
    <path d="M432 230 C 760 330, 760 780, 520 866" fill="none" stroke="var(--line-cyan)" stroke-width="2"/>
    <polyline points="508,858 521,866 506,873" fill="none" stroke="var(--line-cyan)" stroke-width="2"/>
    <line x1="252" y1="866" x2="50" y2="866" stroke="var(--line-cyan)" stroke-width="2"/>
    <polyline points="62,858 49,866 62,874" fill="none" stroke="var(--line-cyan)" stroke-width="2"/>
  </svg>

  <div class="icon-tile icon-tile--top" role="img" aria-label="Icon of an apple resting on a stack of books"></div>

  <h1 class="title">
    <span class="title__small">THE</span>
    <span class="title__main">LINDENMOOR</span>
    <span class="title__sub">COMPASS</span>
  </h1>

  <div class="icon-tile icon-tile--bottom" role="img" aria-label="Icon of a trophy cup with a star"></div>

  <footer class="author-band">
    <p class="author">MARISSA QUINN HALVERT</p>
  </footer>
</main>
</body>
</html>
```